New local Orchid nursery branding

We need a business card designed for our small local company in Darwin, Australia that grows orchids, called Blooms at Carrow.
We will be running private sales from our property, and handing these out at local events for perspective customers.

We would like to see designs that are simple, and able to be used with minimal colours and containing an orchid, preferably a stylised representation instead of a photo.
The eventual hope is to take this into larger formats to create our company logo/branding etc, but for now we just need business cards.

Target Market(s)

Local Orchid

Industry/Entity Type

Business

Contact Information for Business Card

Company Name
Logo
Name
Phone Number
Street Address
Email Address (less prominent than rest of the text)

Font styles to use
Sans Serif

Requirements
Must have
• Name of the company, which is Blooms at Carrow
Nice to have
• stylised orchid logo
Should not have
• too many colours

```html
<!DOCTYPE html>
<html lang="en">
<head>
<meta charset="utf-8">
<title>Blooms at Carrow – Business Card</title>
<link rel="stylesheet" href="https://fonts.googleapis.com/css2?family=Arimo:wght@400;700&display=swap">
<style>
  :root {
    --paper: #ffffff;
    --ink: #000000;
    --brand-blue: #3b4fbf;
    --brand-plum: #4f0e52;
    --lilac: #a981ab;
    --icon-grey: #555555;
  }
  html, body {
    margin: 0;
    padding: 0;
    overflow: hidden;
    background: var(--paper);
  }
  .card {
    position: relative;
    width: 1200px;
    height: 777px;
    background: var(--paper);
    font-family: "Arimo", Arial, Helvetica, sans-serif;
    color: var(--ink);
    overflow: hidden;
  }
  .brand {
    position: absolute;
    left: 34px;
    top: 176px;
    display: flex;
    align-items: center;
    gap: 16px;
  }
  .brand-dot {
    width: 48px;
    height: 48px;
    border-radius: 50%;
    background: var(--brand-plum);
  }
  .brand-name {
    font-size: 48px;
    font-weight: 400;
    color: var(--brand-blue);
    letter-spacing: 1px;
    line-height: 1;
  }
  .contact-name {
    position: absolute;
    left: 72px;
    top: 334px;
    margin: 0;
    font-size: 40px;
    font-weight: 700;
    line-height: 1;
  }
  .contact-lines {
    position: absolute;
    left: 72px;
    top: 410px;
    margin: 0;
    padding: 0;
    list-style: none;
    font-size: 33px;
    line-height: 46px;
  }
  .contact-lines li {
    display: flex;
    align-items: center;
  }
  .contact-icon {
    width: 34px;
    height: 34px;
    margin-right: 16px;
    flex: none;
  }
  .contact-email { font-size: 32px; }
  .address {
    position: absolute;
    left: 72px;
    top: 532px;
    margin: 0;
    font-style: normal;
    font-size: 34px;
    line-height: 44px;
  }
  .address-country { font-weight: 700; }
  .brand-accent {
    position: absolute;
    left: 822px;
    top: 282px;
    width: 330px;
    height: 330px;
    border-radius: 50%;
    background: var(--lilac);
  }
</style>
</head>
<body>
<main class="card">
  <div class="brand">
    <span class="brand-dot" aria-hidden="true"></span>
    <span class="brand-name">Blooms at Carrow</span>
  </div>

  <h1 class="contact-name">Name Here</h1>

  <ul class="contact-lines">
    <li>
      <svg class="contact-icon" viewBox="0 0 34 34" aria-hidden="true">
        <rect x="10" y="7" width="14" height="25" rx="2" fill="none" stroke="var(--icon-grey)" stroke-width="2.4"/>
        <line x1="13" y1="7" x2="13" y2="1" stroke="var(--icon-grey)" stroke-width="2.4"/>
        <rect x="13" y="11" width="8" height="6" fill="var(--icon-grey)"/>
        <g fill="var(--icon-grey)">
          <rect x="13" y="20" width="2" height="2"/><rect x="16" y="20" width="2" height="2"/><rect x="19" y="20" width="2" height="2"/>
          <rect x="13" y="24" width="2" height="2"/><rect x="16" y="24" width="2" height="2"/><rect x="19" y="24" width="2" height="2"/>
        </g>
      </svg>
      <span class="contact-phone">+61 000 000 000</span>
    </li>
    <li>
      <svg class="contact-icon" viewBox="0 0 34 34" aria-hidden="true">
        <rect x="3" y="9" width="28" height="17" fill="none" stroke="var(--icon-grey)" stroke-width="2"/>
        <polyline points="3,9 17,19 31,9" fill="none" stroke="var(--icon-grey)" stroke-width="2"/>
        <polyline points="3,26 13,16 M21,16 31,26" fill="none" stroke="var(--icon-grey)" stroke-width="2"/>
      </svg>
      <span class="contact-email">emailaddresshere@email.com</span>
    </li>
  </ul>

  <address class="address">
    100 Sample Street<br>
    Darwin, NT<br>
    <span class="address-country">Australia</span>
  </address>

  <div class="brand-accent" aria-hidden="true"></div>
</main>
</body>
</html>
```